Flu Brochure- brief and easy-to-read

A team of health educators is looking to design a brochure on what Americans need to "know and do" when it comes to flu season. All copy and images will be provided.

The brochure needs to be an 8.5 x 11 inch bi-fold design.

I am only able to upload up to 5 files. So, additional images will have to sent via dropbox or some other mechanism.

Target Market(s)

The audience is vast, but the content and design need to be simple and engaging.

Industry/Entity Type

Health

Requirements
Must have
• Must Have:
- Clear and Simple, Easy-to-read and Understand and Act on- should be very focused on what the consumer should do about taking care of themselves when it comes to the flu.

We will provide all of the copy for the brochure design. We will also provide photographs for the project.

Captions for photographs that support the key message.

Should Not Have:
- x reverse print- e.g., no white font on a black background
x fancy fonts or heavy use of italics
x use of all capitals
x no full justification
x no use of drop caps

Must be multicultural as well.

```html
<!DOCTYPE html>
<html lang="en">
<head>
<meta charset="utf-8">
<title>Flu Season Brochure</title>
<link href="https://fonts.googleapis.com/css2?family=Source+Sans+3:wght@200;300;400;600;700&display=swap" rel="stylesheet">
<style>
:root{
  --blue:#1f6db5;
  --band:#1a63ad;
  --ink:#333;
  --grey:#555;
  --flu:#bdbdbd;
  --rule:#9bb8d8;
  --red:#d2232a;
  --bg:#ece9e4;
  --paper:#fff;
}
*{box-sizing:border-box;margin:0;padding:0}
html,body{width:1200px;height:796px;overflow:hidden;background:var(--bg);font-family:"Source Sans 3",sans-serif;color:var(--ink)}
.canvas{position:relative;width:1200px;height:796px}
.page{position:absolute;top:69px;width:514px;height:658px;background:var(--paper);box-shadow:0 2px 8px rgba(0,0,0,.18);overflow:hidden}
.page--front{left:75px}
.page--back{left:611px}
.abs{position:absolute}
p,li{font-size:7.4px;line-height:1.4}
ul{list-style:none}
.dot-list li{position:relative;padding-left:12px;margin-bottom:2px}
.dot-list li::before{content:"";position:absolute;left:0;top:2px;width:6px;height:6px;border-radius:50%;background:#333}
.ring-list li{margin-bottom:3px}
.ring-list li::before{background:var(--blue)}

/* front */
.agency{left:40px;top:31px;display:flex;align-items:center;gap:10px}
.agency__mark{width:91px;height:55px;background:var(--blue)}
.agency__name{font-size:16.5px;font-weight:400;color:#222;line-height:1}
.agency__tag{font-size:8.5px;color:#444;margin-top:4px}
.hero-photo{left:0;top:105px;width:295px;height:182px;border-bottom-left-radius:14px;background:linear-gradient(135deg,#e9e6e1 0%,#d9cfc3 45%,#b7a89a 100%)}
.flu-word{left:292px;top:118px;font-size:104px;font-weight:200;color:var(--flu);letter-spacing:2px;line-height:1}
.facts{left:298px;top:258px;width:205px}
.facts h2{font-size:21px;font-weight:400;color:var(--blue);line-height:1.2;margin-bottom:8px}
.facts h3{font-size:10px;font-weight:700;margin:7px 0 4px}
.facts .note{margin-top:8px}
.question{left:36px;top:306px;font-size:23.5px;font-weight:300;color:var(--grey);line-height:33px}
.question .accent{font-size:34px;color:var(--blue)}
.steps{left:36px;top:510px}
.steps li{font-size:19px;font-weight:600;color:var(--blue);line-height:26px;padding-left:24px;position:relative}
.steps li::before{content:"";position:absolute;left:0;top:7px;width:12px;height:12px;border:3px solid var(--blue);border-radius:50%}
.partner{left:298px;top:545px;font-size:22px;font-weight:400;color:var(--red)}
.credit{left:160px;top:583px;width:342px;border-top:1px solid #999;padding-top:4px}
.credit p{font-size:6.3px;line-height:1.35}
.band{left:0;bottom:0;width:100%;background:var(--band);color:#fff}
.band--front{height:41px;text-align:right;padding:9px 26px 0 0;font-size:17px;font-weight:300;letter-spacing:1.5px}

/* back */
.back-title{left:35px;top:30px;font-size:23px;font-weight:600;color:var(--blue)}
.back-intro{left:35px;top:75px}
.divider{left:0;top:107px;width:514px;height:4px;border-top:1px solid var(--rule);border-bottom:1px solid var(--rule)}
.photo{top:117px;height:164px}
.photo--care{left:0;width:142px;background:linear-gradient(160deg,#f0ece8,#c9b3a4 60%,#7f9fb9)}
.photo--kids{left:146px;width:222px;background:linear-gradient(160deg,#f4f1ee,#e6c2a8 50%,#6fa8c8)}
.photo--shot{left:371px;width:143px;background:linear-gradient(160deg,#efeae6,#c59b86 50%,#5aa58c)}
.col{width:200px}
.col h2{font-size:23px;font-weight:400;color:var(--blue);line-height:1.15;margin-bottom:7px}
.col h3{font-size:10px;font-weight:700;margin:5px 0 4px}
.col p{margin-bottom:2px}
.prevent{left:35px;top:302px}
.protect{left:35px;top:458px}
.treat{left:283px;top:302px;width:205px}
.self-care{left:283px;top:412px;width:205px}
.self-care h2{font-size:19px;line-height:1.2}
.vrule{left:257px;top:300px;width:1px;height:292px;background:#bbb}
.goto{left:283px;top:584px;font-size:12px;letter-spacing:.3px;color:#333}
.goto strong{font-weight:700}
.band--back{height:50px;padding:0 0 0 32px;font-size:14px;font-weight:600;display:flex;gap:14px;align-items:center}
.band--back .phone{font-size:17px;font-weight:700;letter-spacing:.5px}
</style>
</head>
<body>
<div class="canvas">

  <section class="page page--front">
    <div class="agency abs">
      <div class="agency__mark"></div>
      <div>
        <div class="agency__name">National Health Protection Agency</div>
        <div class="agency__tag">NHPA: Healthy Homes. Stronger Communities.™</div>
      </div>
    </div>

    <div class="hero-photo abs" role="img" aria-label="Woman wrapped in a blanket blowing her nose and holding a thermometer"></div>
    <div class="flu-word abs">FLU</div>

    <div class="facts abs">
      <h2>Know… the facts:</h2>
      <h3>The flu is a virus</h3>
      <p>If you get the flu, you may not feel that bad, but sometimes the flu can make you so sick that you can die.</p>
      <p>You catch flu from other people.</p>
      <p>People with flu spread it by coughing, sneezing, or spreading their germs.</p>
      <h3>Know- common complaints for flu:</h3>
      <p>fever, cough, sore throat, runny or stuffy nose, headaches, body aches, chills, being tired</p>
      <h3>Know- the warning signs:</h3>
      <ul class="dot-list ring-list">
        <li>hard time breathing or short of breath</li>
        <li>pain or pressure in the chest or stomach</li>
        <li>feeling dizzy all of a sudden</li>
        <li>becoming confused</li>
      </ul>
      <p class="note">If you have ANY of the warning signs, contact your doctor!<br>(maybe this would go into a call out box)</p>
    </div>

    <div class="question abs">What are 4 things<br>I can do to prepare for<br>the flu season and<br>keep <span class="accent">my family</span><br><span class="accent">healthy?</span></div>

    <ul class="steps abs">
      <li>Know</li>
      <li>Prevent</li>
      <li>Protect</li>
      <li>Treat</li>
    </ul>

    <div class="partner abs">Harlow &amp; Finch</div>

    <div class="credit abs">
      <p>©2013. Riverbend Health Literacy Team. Riverbend University: Marlow T, Okafor J, Lind S. Content based on scientific evidence from the National Health Department and the National Health Protection Agency (NHPA) as of March 2013.</p>
    </div>

    <div class="band band--front abs">Go to: http://www.healthprotect.org/flu/</div>
  </section>

  <section class="page page--back">
    <h1 class="back-title abs">Once you start feeling better…</h1>
    <ul class="back-intro dot-list abs">
      <li>You still want to make sure you don't get other people sick.</li>
      <li>Stay at home until you are "fever-free" for at least 24 hours without the help of medicine.</li>
    </ul>
    <div class="divider abs"></div>

    <div class="photo photo--care abs" role="img" aria-label="Nurse giving an older woman a flu shot in the arm"></div>
    <div class="photo photo--kids abs" role="img" aria-label="Group of smiling children from different backgrounds"></div>
    <div class="photo photo--shot abs" role="img" aria-label="Health worker giving a girl a nasal spray flu vaccine"></div>

    <div class="col prevent abs">
      <h2>Prevent</h2>
      <p>How Can I Keep Me And My Family From Getting Flu?</p>
      <p>Be sure everyone 6 months and older gets a flu shot. You can get a flu shot through a needle or a spray.</p>
      <p>The flu shot helps protect you against the three most common types of flu.</p>
      <h3>The shot…</h3>
      <ul class="dot-list">
        <li>is very important for pregnant women, and</li>
        <li>you don't need a prescription for it!</li>
      </ul>
    </div>

    <div class="col protect abs">
      <h2>Protect</h2>
      <h3>How Do I Protect My Family?</h3>
      <ul class="dot-list">
        <li>Stay away from sick people.</li>
        <li>Wash your hands with soap and water or hand sanitizer when you eat, cough or go to the bathroom.</li>
        <li>Try not to touch your eyes, nose or mouth because that is how you catch flu.</li>
        <li>Cough or sneeze into your sleeve or cover your nose and mouth with a tissue. Throw the tissue in the trash!</li>
      </ul>
    </div>

    <div class="vrule abs"></div>

    <div class="col treat abs">
      <h2>Treat</h2>
      <p>What If Someone Has The Flu?</p>
      <p>If you think someone in your family has the flu, call your doctor.</p>
      <ul class="dot-list" style="margin-top:8px">
        <li>Ask if they need to be seen.</li>
        <li>Ask your doctor about flu medicine.</li>
      </ul>
    </div>

    <div class="col self-care abs">
      <h2>If Your Doctor Tells You<br>To Treat Yourself…</h2>
      <p>Stay home and rest – don't spread your germs to others!</p>
      <p>Take medicines for fever, such as acetaminophen (Feverex®) or ibuprofen (Painaway®, Ibucare®, Relivo®).</p>
      <h3>Do not take aspirin for fever.</h3>
      <ul class="dot-list">
        <li>Drink 6-8 big glasses of water, juice, or sports drink (like Hydrade®, Electrolite®) every day.</li>
        <li>If around other people, wear a mask.</li>
      </ul>
    </div>

    <div class="goto abs">Go to: <strong>http://www.healthprotect.org/flu/</strong></div>

    <div class="band band--back abs">
      <span>For reliable info on flu: Call your doctor</span>
      <span>• Call: <span class="phone">1-800-555-0142</span></span>
    </div>
  </section>

</div>
</body>
</html>
```